Fire Protection Company

Hi we have a company called Brenlow Protection Services and are looking for a new design we are wanting flames as the last card was great with the whole background flames but you cant really see the services offered, phone, names etc.

We need something more upmarket and professional and only have a small budget

We need the words Brenlow Protection Services, Marcus Pelwey MSBuildA - Fire Safety Consultant, Phone No 0427316508 address : PO Box 8163 TRDC 4852 ABN 71264085319, HVRA Lic.5382410 Email marcus@brenlowgroup.example.com.au

Industry/Entity Type

Fire Safety

Font styles to use
Sans Serif

Colors
ec2027
ffc214

```html
<!DOCTYPE html>
<html lang="en">
<head>
<meta charset="utf-8">
<title>Brenlow Protection Services – Business Card</title>
<link href="https://fonts.googleapis.com/css2?family=Arimo:wght@400;700&display=swap" rel="stylesheet">
<style>
  :root {
    --backdrop: #4a4a4a;
    --card-white: #f4f4f4;
    --ink: #2b2b2b;
    --brand-red: #ec2027;
    --brand-yellow: #ffc214;
    --flame-deep: #7a1e06;
    --flame-mid: #e0560e;
    --flame-bright: #ffb01f;
    --divider: #1f1f1f;
  }
  * { box-sizing: border-box; margin: 0; padding: 0; }
  html, body {
    width: 1200px; height: 900px; overflow: hidden;
    background: var(--backdrop);
    font-family: "Arimo", Arial, sans-serif;
  }
  .business-card {
    position: absolute; left: 100px; top: 165px;
    width: 1000px; height: 570px;
    background: var(--card-white);
    box-shadow: 0 20px 50px rgba(0,0,0,.45);
    overflow: hidden;
  }
  .flame-band {
    position: absolute; left: 0; top: 0; width: 100%; height: 330px;
    background:
      radial-gradient(ellipse at 30% 60%, var(--flame-bright) 0%, transparent 45%),
      radial-gradient(ellipse at 75% 40%, var(--flame-bright) 0%, transparent 40%),
      radial-gradient(ellipse at 55% 90%, #ffd34a 0%, transparent 35%),
      linear-gradient(180deg, var(--flame-deep) 0%, var(--flame-mid) 55%, #f08a18 100%);
  }
  .brand {
    position: absolute; left: 0; right: 0; top: 95px;
    text-align: center; color: var(--brand-yellow); font-weight: 700;
  }
  .brand-name { font-size: 96px; letter-spacing: 6px; line-height: 1; }
  .brand-tagline { font-size: 30px; letter-spacing: 3px; margin-top: 10px; }
  .band-divider {
    position: absolute; left: 0; top: 330px; width: 100%; height: 10px;
    background: var(--divider);
    box-shadow: 0 4px 8px rgba(0,0,0,.35);
  }
  .consultant {
    position: absolute; left: 50px; top: 390px;
    letter-spacing: 2px;
  }
  .consultant-name { font-size: 30px; color: var(--ink); }
  .consultant-role { font-size: 20px; color: var(--brand-red); margin-top: 4px; }
  .registrations { margin-top: 34px; font-size: 20px; color: var(--ink); line-height: 1.4; }
  .registrations .label { color: var(--brand-red); }
  .contact-list {
    position: absolute; left: 560px; top: 380px;
    list-style: none; font-size: 24px; color: var(--ink); letter-spacing: 2px;
  }
  .contact-list li { display: flex; align-items: center; height: 40px; white-space: nowrap; }
  .contact-list .email { font-size: 20px; letter-spacing: 1px; }
  .contact-icon { width: 32px; height: 32px; margin-right: 12px; flex: none; }
</style>
</head>
<body>
  <section class="business-card">
    <div class="flame-band" role="img" aria-label="Photograph of bright orange and yellow flames filling the card header"></div>
    <div class="brand">
      <div class="brand-name">BRENLOW</div>
      <div class="brand-tagline">PROTECTION SERVICES</div>
    </div>
    <div class="band-divider"></div>

    <div class="consultant">
      <div class="consultant-name">Marcus Pelwey MSBuildA</div>
      <div class="consultant-role">FIRE SAFETY CONSULTANT</div>
      <div class="registrations">
        <div><span class="label">ABN</span> 71264085319</div>
        <div><span class="label">HVRA LIC.</span>5382410</div>
      </div>
    </div>

    <ul class="contact-list">
      <li>
        <svg class="contact-icon" viewBox="0 0 32 32" aria-hidden="true">
          <rect width="32" height="32" rx="5" fill="var(--brand-red)"/>
          <path d="M7 12c0-3 4-4 9-4s9 1 9 4v2h-5v-2h-8v2H7z" fill="#fff"/>
          <rect x="9" y="16" width="14" height="9" rx="2" fill="#fff"/>
          <circle cx="16" cy="20.5" r="2.2" fill="var(--brand-red)"/>
        </svg>
        042 731 6508
      </li>
      <li class="email">
        <svg class="contact-icon" viewBox="0 0 32 32" aria-hidden="true">
          <rect width="32" height="32" rx="5" fill="var(--brand-red)"/>
          <rect x="6" y="9" width="20" height="14" rx="1.5" fill="#fff"/>
          <path d="M6 10l10 8 10-8" fill="none" stroke="var(--brand-red)" stroke-width="2"/>
        </svg>
        marcus@brenlowgroup.example.com.au
      </li>
      <li>
        <svg class="contact-icon" viewBox="0 0 32 32" aria-hidden="true">
          <rect width="32" height="32" rx="5" fill="var(--brand-red)"/>
          <path d="M16 6L5 16h3v10h6v-6h4v6h6V16h3z" fill="#fff"/>
        </svg>
        PO Box 8163 TRDC 4852
      </li>
    </ul>
  </section>
</body>
</html>
```